Speisekarten für ein modernes, junges Café
Zielgruppe
Wir suchen eine Speisekarte für ein modernes, junges Café. Frühstück, kleine Speisen, Snacks und Getränke stehen auf der Karte. Unsere Zielgruppe sind hauptsächlich junge Menschen bis 40 Jahre.
Die Speisekarte sollte immer änderbar sein ( nur Text bei neuen Speisen zum Beispiel )
Aufgabenstellung
Das Logo kann und soll gerne mit eingefügt werden. Eventuell gleich auf dem Deckblatt.
Generell bin ich offen für junge, coole Ideen.
Unten die Themen/ grobe Überschriften
Kaffee und Espresso
Frühstücksvariationen
Eierspeisen
Frühstück zum löffeln
Pancakes
Extras zum Frühstück
Snacks/ kleine Speisen
-die Kurbel. Drinks
-die Kurbel. Wein & Bier )
((Kinderspeisekarte:
zusätzlich noch ein extra Blatt für die Kinder zum ausmalen mit den illustrierten Bildern auch im modernen Stil ))

```html
<!DOCTYPE html>
<html lang="de">
<head>
<meta charset="utf-8">
<title>die Kurbel. – Speisekarte</title>
<link rel="stylesheet" href="https://fonts.googleapis.com/css2?family=Cormorant+Garamond:ital,wght@0,400;0,500;1,400&family=Montserrat:wght@500&family=Mrs+Saint+Delafield&display=swap">
<style>
  :root {
    --backdrop: #dcd8d2;
    --paper: #f1f1ef;
    --ink: #1f1c1a;
    --muted: #555049;
    --sand: #cfbb9f;
  }
  * { margin: 0; padding: 0; box-sizing: border-box; }
  html, body { width: 1200px; height: 739px; overflow: hidden; }
  body { background: var(--backdrop); position: relative; font-family: "Cormorant Garamond", serif; color: var(--ink); }

  .page {
    position: absolute; top: 113px; width: 369px; height: 483px;
    background: var(--paper);
    box-shadow: 0 2px 10px rgba(0,0,0,.18);
  }
  .page--cover { left: 194px; }
  .page--menu { left: 637px; }

  .cover-name {
    position: absolute; left: 0; right: 0; top: 218px;
    text-align: center; font-size: 38px; font-weight: 500; letter-spacing: 1px;
  }

  .menu-brand {
    position: absolute; left: 0; right: 0; top: 34px;
    text-align: center; font-size: 16px; font-weight: 500;
  }
  .menu-title-script {
    position: absolute; left: 0; right: 0; top: 185px;
    text-align: center; font-family: "Mrs Saint Delafield", cursive; font-size: 30px; line-height: 1;
  }
  .menu-title {
    position: absolute; left: 0; right: 0; top: 211px;
    text-align: center; font-size: 31px; letter-spacing: 3px; line-height: 1;
  }
  .menu-title-script { top: 72px; }
  .menu-title { top: 98px; }

  .section { position: absolute; width: 129px; }
  .section-head {
    background: var(--sand); height: 20px; line-height: 20px;
    text-align: center; font-size: 11.5px; letter-spacing: 1.6px; text-transform: uppercase;
    margin-bottom: 10px;
  }
  .item { position: relative; height: 26.4px; }
  .item-name {
    font-family: "Montserrat", sans-serif; font-size: 6.2px; letter-spacing: 1.3px;
    text-transform: uppercase; line-height: 8px;
  }
  .item-desc { font-style: italic; font-size: 6.8px; color: var(--muted); line-height: 9px; }
  .item-price {
    position: absolute; right: 0; top: 0;
    font-family: "Montserrat", sans-serif; font-size: 5.8px; letter-spacing: 1px; line-height: 8px;
  }
  .item-price::before { content: "// "; }

  .section--starters { left: 42px; top: 155px; }
  .section--mains { left: 201px; top: 155px; }
  .section--drinks { left: 40px; top: 314px; }
  .section--desserts { left: 199px; top: 366px; }
  .section--mains .item:nth-child(6) { margin-top: 1.5px; }
</style>
</head>
<body>

<section class="page page--cover">
  <div class="cover-name">die Kurbel.</div>
</section>

<section class="page page--menu">
  <div class="menu-brand">die Kurbel.</div>
  <div class="menu-title-script">Speise</div>
  <h1 class="menu-title" style="font-weight:400">KARTE</h1>

  <div class="section section--starters">
    <div class="section-head">Vorspeise</div>
    <div class="item"><div class="item-name">Bruscetta</div><div class="item-desc">mit frischem Basilikum</div><div class="item-price">7 €</div></div>
    <div class="item"><div class="item-name">Kürbissuppe</div><div class="item-desc">mit Kokosmilch</div><div class="item-price">6 €</div></div>
    <div class="item"><div class="item-name">Quinoa-Salat</div><div class="item-desc">mit Süßkartoffel Pommes</div><div class="item-price">6,50 €</div></div>
    <div class="item"><div class="item-name">Tomatensuppe</div><div class="item-desc">mit Kräutercroutons</div><div class="item-price">6,50 €</div></div>
  </div>

  <div class="section section--mains">
    <div class="section-head">Hauptspeise</div>
    <div class="item"><div class="item-name">Erbsen-Curry</div><div class="item-desc">mit Basmati Reis</div><div class="item-price">13 €</div></div>
    <div class="item"><div class="item-name">Soja-Nudeln</div><div class="item-desc">mit Cashew-Sauce</div><div class="item-price">14 €</div></div>
    <div class="item"><div class="item-name">Bohnenburger</div><div class="item-desc">mit Süßkartoffel Pommes</div><div class="item-price">16,50 €</div></div>
    <div class="item"><div class="item-name">Risotto</div><div class="item-desc">mit Pilzen &amp; Kürbis</div><div class="item-price">12,50 €</div></div>
    <div class="item"><div class="item-name">Hähnchenbrust</div><div class="item-desc">mit Rosmarinkartoffeln</div><div class="item-price">13,50 €</div></div>
    <div class="item"><div class="item-name">Lachsfilet</div><div class="item-desc">mit Kartoffelpüree</div><div class="item-price">14,50 €</div></div>
  </div>

  <div class="section section--drinks">
    <div class="section-head">Getränke</div>
    <div class="item"><div class="item-name">Softgetränk</div><div class="item-desc">Cola, Orangenlimo, Zitronenlimo</div><div class="item-price">3 €</div></div>
    <div class="item"><div class="item-name">Mineralwasser</div><div class="item-desc">0,75 Liter</div><div class="item-price">5 €</div></div>
    <div class="item"><div class="item-name">Orangensaft</div><div class="item-desc">frisch gepresst</div><div class="item-price">6,50 €</div></div>
    <div class="item"><div class="item-name">Kaffee</div><div class="item-desc">verschiedene Sorten</div><div class="item-price">2,50 €</div></div>
    <div class="item"><div class="item-name">Bier</div><div class="item-desc">0,5 Liter</div><div class="item-price">5,50 €</div></div>
  </div>

  <div class="section section--desserts">
    <div class="section-head">Dessert</div>
    <div class="item"><div class="item-name">Schokomousse</div><div class="item-desc">mit Beeren und Sahne</div><div class="item-price">7 €</div></div>
    <div class="item"><div class="item-name">Vanilleeis</div><div class="item-desc">mit heißen Kirschen</div><div class="item-price">5 €</div></div>
    <div class="item"><div class="item-name">Apfelstrudel</div><div class="item-desc">mit Vanillesauce</div><div class="item-price">6,50 €</div></div>
  </div>
</section>

</body>
</html>
```